MO&A - Business Card and Stationery for a Law Firm
Mendívil Ortuzar & Asociados
Professional
Julián Esteban Mendívil Ortuzar
Abogado
Carrera 48 No. 62-14 Of. 305
Bogotá D.C., Colombia
julian.mendivil@mendivilortuzar.com
www.mendivilortuzar.com
The text on the back of the card is in Spanish, for your information the meaning in English is as follows:
Companies in Colombia and abroad.
International business.
Tax planning.
Foreign investments.
Inmigration.
Industrial property.
Please distribute the text as you consider.
Logo and the following text:
Sociedades en Colombia y el exterior.
Negocios internacionales.
Planeación tributaria.
Inversión extranjera.
Asuntos migratorios.
Propiedad Industrial.

```html
<!DOCTYPE html>
<html lang="es">
<head>
<meta charset="utf-8">
<title>Mendívil Ortuzar &amp; Asociados — Tarjeta</title>
<link rel="stylesheet" href="https://fonts.googleapis.com/css2?family=Open+Sans:wght@400;600;700&display=swap">
<style>
  :root {
    --navy: #1b2a57;
    --ink: #4a4f5c;
    --paper: #ffffff;
    --backdrop: #e9e7e3;
    --rule: #9aa0ad;
  }
  * { margin: 0; padding: 0; box-sizing: border-box; }
  html, body { width: 1200px; height: 914px; overflow: hidden; background: var(--backdrop); }
  body { font-family: "Open Sans", Arial, sans-serif; color: var(--ink); }

  .card {
    position: absolute; left: 100px; top: 167px;
    width: 1000px; height: 580px;
    background: var(--paper);
    box-shadow: 0 6px 24px rgba(0,0,0,.18);
    overflow: hidden;
  }

  .brand {
    position: absolute; left: 330px; top: 110px;
    display: flex; align-items: center; gap: 22px;
  }
  .brand-square { width: 92px; height: 92px; background: var(--navy); flex: none; }
  .brand-name {
    font-family: "Open Sans", Arial, sans-serif;
    font-weight: 600; color: var(--navy);
    font-size: 30px; line-height: 1.2; letter-spacing: 1px;
    text-transform: uppercase;
  }

  .person {
    position: absolute; right: 530px; top: 300px;
    text-align: right; font-size: 19px; line-height: 1.55;
  }
  .person-name { color: var(--navy); font-weight: 700; font-size: 22px; margin-bottom: 2px; }

  .divider {
    position: absolute; left: 497px; top: 300px;
    width: 1px; height: 150px; background: var(--rule);
  }

  .contacts {
    position: absolute; left: 520px; top: 306px;
    list-style: none; font-size: 17px; line-height: 1;
  }
  .contacts li { display: flex; align-items: center; gap: 12px; height: 33px; }
  .contacts svg { width: 18px; height: 18px; fill: var(--navy); flex: none; }

  .band { position: absolute; left: 0; top: 478px; width: 1000px; height: 70px; }
</style>
</head>
<body>
  <div class="card">
    <div class="brand">
      <div class="brand-square"></div>
      <div class="brand-name">Mendívil Ortuzar<br>&amp; Asociados</div>
    </div>

    <div class="person">
      <p class="person-name">Julián Esteban Mendívil Ortuzar</p>
      <p>Abogado</p>
      <p>Carrera 48 No. 62-14 Of. 305</p>
      <p>Bogotá D.C., Colombia</p>
    </div>

    <div class="divider"></div>

    <ul class="contacts">
      <li><svg viewBox="0 0 24 24"><path d="M6.6 10.8a15 15 0 0 0 6.6 6.6l2.2-2.2a1 1 0 0 1 1-.25 11.4 11.4 0 0 0 3.6.57 1 1 0 0 1 1 1V20a1 1 0 0 1-1 1A17 17 0 0 1 3 4a1 1 0 0 1 1-1h3.5a1 1 0 0 1 1 1c0 1.25.2 2.45.57 3.57a1 1 0 0 1-.25 1z"/></svg>+57 (1) 555 0142</li>
      <li><svg viewBox="0 0 24 24"><path d="M7 1h10a2 2 0 0 1 2 2v18a2 2 0 0 1-2 2H7a2 2 0 0 1-2-2V3a2 2 0 0 1 2-2zm0 3v14h10V4zm5 15.5a1 1 0 1 0 0 2 1 1 0 0 0 0-2z"/></svg>+57 300 555 0199</li>
      <li><svg viewBox="0 0 24 24"><path d="M2 5h20v14H2zm2 2v.5l8 5 8-5V7zm0 2.8V17h16V9.8l-8 5z"/></svg>julian.mendivil@mendivilortuzar.com</li>
      <li><svg viewBox="0 0 24 24"><path d="M12 2a10 10 0 1 0 0 20 10 10 0 0 0 0-20zm6.9 9h-3a15 15 0 0 0-1.3-5.6A8 8 0 0 1 18.9 11zM12 4.1c.9 1.3 1.8 3.6 1.9 6.9h-3.8c.1-3.3 1-5.6 1.9-6.9zM9.4 5.4A15 15 0 0 0 8.1 11h-3a8 8 0 0 1 4.3-5.6zM5.1 13h3a15 15 0 0 0 1.3 5.6A8 8 0 0 1 5.1 13zm6.9 6.9c-.9-1.3-1.8-3.6-1.9-6.9h3.8c-.1 3.3-1 5.6-1.9 6.9zm2.6-1.3a15 15 0 0 0 1.3-5.6h3a8 8 0 0 1-4.3 5.6z"/></svg>www.mendivilortuzar.com</li>
    </ul>

    <svg class="band" viewBox="0 0 1000 70" preserveAspectRatio="none" aria-hidden="true">
      <polygon points="0,0 492,0 480,70 0,70" fill="var(--navy)"/>
      <polygon points="500,0 1000,0 1000,70 488,70" fill="var(--navy)"/>
    </svg>
  </div>
</body>
</html>
```